The Festival! Poster for an Annual Dance Showcase

We are looking for a dynamic festival/concert style poster for our annual dance showcase featuring at least one image of our dancers and the main information. The main image should be one of the dancers but there can be a collage of the dancers or smaller images around the poster. I have included some reference images but it can vary from them.

Must have this information;
Date - May 22-26
Location - Mabel Corwin Hale Theatre
Tickets - Vondo.bm

Target Market(s)

Parents and people who love dance

Industry/Entity Type

Dance

Font styles to use
Sans Serif

Colors
E54698
E96AAD
F1A4CE
F9D9EA
FCEFF6

Requirements
Must have
• Logo, Date and Location, Picture of Dancer

```html
<!DOCTYPE html>
<html lang="en">
<head>
<meta charset="utf-8">
<title>Annual Dance Showcase</title>
<link rel="stylesheet" href="https://fonts.googleapis.com/css2?family=Montserrat:wght@600;800;900&family=Open+Sans:wght@600;700;800&display=swap">
<style>
  :root {
    --violet-deep: #4d066b;
    --violet: #7a1690;
    --orchid: #a64aa6;
    --cream: #fdf3d6;
    --rose: #c97d7a;
    --glow: #ffcf1f;
    --glow-soft: #fff09a;
    --teal: #1ee0b3;
    --ticket: #f7e04a;
    --pink-line: #f08ad0;
  }
  * { margin: 0; padding: 0; box-sizing: border-box; }
  html, body { width: 848px; height: 1200px; overflow: hidden; background: var(--violet-deep); }
  .poster {
    position: relative;
    width: 848px;
    height: 1200px;
    overflow: hidden;
    font-family: "Open Sans", sans-serif;
    background:
      radial-gradient(ellipse 70% 45% at 60% 45%, rgba(180,80,170,.55), transparent 70%),
      linear-gradient(170deg, var(--violet-deep) 0%, var(--violet) 25%, var(--orchid) 55%, var(--violet) 80%, var(--violet-deep) 100%);
  }
  .streaks { position: absolute; inset: 0; }
  .dancer-photo {
    position: absolute;
    left: 150px;
    top: 230px;
    width: 420px;
    height: 900px;
    border-radius: 48% 52% 30% 40% / 30% 30% 20% 20%;
    background: linear-gradient(180deg, rgba(120,70,55,.55) 0%, rgba(20,80,120,.7) 40%, rgba(20,90,130,.75) 100%);
  }
  .brand {
    position: absolute;
    left: 70px;
    top: 150px;
    transform: rotate(-15deg);
    transform-origin: left top;
    color: var(--cream);
    font-family: "Montserrat", sans-serif;
    display: flex;
    align-items: center;
    gap: 10px;
  }
  .brand-mark { width: 26px; height: 26px; border-radius: 50%; background: #ffffff; }
  .brand-name { font-weight: 800; font-size: 30px; line-height: 1; color: #ffffff; }
  .brand-sub { display: block; font-weight: 800; font-size: 17px; color: #ffffff; letter-spacing: .5px; }
  .presents {
    position: absolute;
    left: 80px;
    top: 275px;
    transform: rotate(-19deg);
    transform-origin: left top;
    color: var(--cream);
    font-family: "Montserrat", sans-serif;
    font-weight: 800;
    font-size: 54px;
    letter-spacing: 28px;
  }
  .title {
    position: absolute;
    transform: rotate(-21deg);
    transform-origin: left bottom;
    font-family: "Montserrat", sans-serif;
    font-weight: 900;
    line-height: 1;
    color: var(--rose);
    -webkit-text-stroke: 3px var(--glow-soft);
    text-shadow: 0 0 8px var(--glow), 0 0 22px var(--glow), 5px 5px 0 rgba(255,230,120,.6);
    white-space: nowrap;
  }
  .title-annual { left: 70px; top: 340px; font-size: 122px; }
  .title-dance { left: 160px; top: 470px; font-size: 128px; }
  .title-showcase { left: -10px; top: 640px; font-size: 138px; }
  .date {
    position: absolute;
    right: 50px;
    top: 795px;
    text-align: right;
    color: var(--teal);
    font-weight: 800;
    line-height: 1;
  }
  .date-range { font-size: 74px; letter-spacing: -1px; }
  .date-range sup { font-size: 36px; vertical-align: 32px; }
  .date-month { display: block; font-size: 72px; margin-top: 4px; }
  .venue {
    position: absolute;
    right: 52px;
    top: 1030px;
    text-align: right;
    color: var(--cream);
    font-weight: 700;
    font-size: 52px;
    line-height: 1.18;
  }
  .tickets {
    position: absolute;
    left: 52px;
    top: 1075px;
    color: var(--ticket);
    font-weight: 700;
  }
  .tickets-label { font-size: 20px; }
  .tickets-site { display: block; font-size: 40px; font-weight: 800; margin-top: 2px; }
</style>
</head>
<body>
<main class="poster">
  <svg class="streaks" width="848" height="1200" viewBox="0 0 848 1200" aria-hidden="true">
    <g stroke-linecap="round">
      <line x1="615" y1="302" x2="848" y2="240" stroke="var(--teal)" stroke-width="10"/>
      <line x1="560" y1="360" x2="848" y2="282" stroke="var(--cream)" stroke-width="7"/>
      <line x1="500" y1="385" x2="848" y2="290" stroke="var(--cream)" stroke-width="3"/>
      <line x1="600" y1="440" x2="848" y2="375" stroke="var(--cream)" stroke-width="6"/>
      <line x1="640" y1="470" x2="848" y2="410" stroke="var(--teal)" stroke-width="5"/>
      <line x1="0" y1="505" x2="200" y2="460" stroke="var(--cream)" stroke-width="2"/>
      <line x1="390" y1="750" x2="848" y2="630" stroke="var(--teal)" stroke-width="3"/>
      <line x1="0" y1="800" x2="330" y2="710" stroke="var(--cream)" stroke-width="7"/>
      <line x1="0" y1="870" x2="270" y2="800" stroke="var(--teal)" stroke-width="22"/>
    </g>
    <g stroke="var(--pink-line)" stroke-width="1.5">
      <line x1="0" y1="395" x2="55" y2="425"/><line x1="0" y1="410" x2="48" y2="437"/>
      <line x1="0" y1="425" x2="40" y2="448"/><line x1="20" y1="375" x2="80" y2="405"/>
      <line x1="40" y1="365" x2="100" y2="395"/>
      <line x1="630" y1="700" x2="680" y2="730"/><line x1="660" y1="690" x2="710" y2="720"/>
      <line x1="690" y1="680" x2="740" y2="710"/><line x1="720" y1="670" x2="770" y2="700"/>
      <line x1="750" y1="660" x2="800" y2="690"/><line x1="780" y1="650" x2="830" y2="680"/>
      <line x1="810" y1="640" x2="848" y2="662"/>
    </g>
  </svg>

  <div class="dancer-photo" role="img" aria-label="Photograph of a dancer in a teal two-piece costume leaping with one arm extended upward"></div>

  <div class="brand">
    <span class="brand-mark"></span>
    <div>
      <span class="brand-name">STRIDE ARC</span>
      <span class="brand-sub">SCHOOL OF DANCE</span>
    </div>
  </div>

  <div class="presents">PRESENTS</div>

  <h1>
    <span class="title title-annual">ANNUAL</span>
    <span class="title title-dance">DANCE</span>
    <span class="title title-showcase">SHOWCASE</span>
  </h1>

  <p class="date">
    <span class="date-range">22<sup>nd</sup>-26<sup>th</sup></span>
    <span class="date-month">May</span>
  </p>

  <p class="venue">Mabel Corwin Hale<br>Theatre</p>

  <p class="tickets">
    <span class="tickets-label">Tickets available at</span>
    <span class="tickets-site">Vondo.bm</span>
  </p>
</main>
</body>
</html>
```